Commercial janitorial cleaning

Janitorial cleaning particularly for commercial buildings. Website needs to specify free estimates. Location of service is Hudson, Valatie, East Greenbush, Troy, Albany ny area. Services page with Janitorial services- General Office Cleaning, Construction Cleaning, Carpet Extraction, Consultation/Business, Lighting Maintenance, Seasonal Deep Cleaning, Window cleaning, Event Cleaning, Floor and Carpet Cleaning, Floor Striping and Waxing. Contact us page with email phone number on page and a request page that emails me if they have any questions. About us page-the picture of my family on it with a section I can type a story myself.

Target Market(s)

Commercial businesses

Industry/Entity Type

Janitorial Service

Number of Pages Required

4 page

Font styles to use
Serif
Sans Serif
Script

Colors
ec1f27
1b1b1b
ffffff
9d9d9d

Requirements
Must have
• Phone number 555-304-7162. Must have free estimates on home page. Going for industrial / modern look to website
Nice to have
• Logo is a red and black building so if those colors could be coordinated to website that would be awesome.

```html
<!DOCTYPE html>
<html lang="en">
<head>
<meta charset="utf-8">
<title>Brightkeep Cleaning Services</title>
<link rel="stylesheet" href="https://fonts.googleapis.com/css2?family=Open+Sans:ital,wght@0,400;0,600;0,700;1,400&family=Lato:wght@400;700&display=swap">
<style>
:root{
  --red:#ec1f27;
  --ink:#1b1b1b;
  --white:#ffffff;
  --grey:#9d9d9d;
  --paper:#f1f1f1;
  --night:#0b0b0b;
}
*{box-sizing:border-box;margin:0;padding:0}
html,body{width:1200px;height:2605px;overflow:hidden}
body{font-family:"Lato",Arial,sans-serif;color:var(--ink);background:var(--white);position:relative}
.abs{position:absolute}

/* header */
.site-header{position:absolute;left:0;top:0;width:1200px;height:134px;background:var(--white);border-bottom:3px solid var(--red)}
.brand{position:absolute;left:82px;top:20px;display:flex;align-items:center;gap:14px}
.brand-mark{width:56px;height:56px;background:var(--red)}
.brand-name{font-family:"Open Sans",sans-serif;font-weight:700;font-size:17px;line-height:19px;color:var(--ink)}
.top-contact{position:absolute;top:24px;display:flex;align-items:center;gap:10px;font-size:14px;color:var(--ink)}
.top-contact .ring{width:30px;height:30px;border:2px solid var(--red);border-radius:50%;display:flex;align-items:center;justify-content:center}
.quote-btn{position:absolute;left:945px;top:21px;width:175px;height:35px;background:var(--red);color:var(--white);font-family:"Open Sans",sans-serif;font-weight:700;font-size:16px;display:flex;align-items:center;justify-content:center}
.main-nav{position:absolute;left:396px;top:78px;width:804px;height:56px;background:var(--ink);clip-path:polygon(28px 0,100% 0,100% 100%,0 100%,12px 20px)}
.main-nav a{position:absolute;top:0;height:56px;display:flex;align-items:center;justify-content:center;color:var(--white);font-family:"Open Sans",sans-serif;font-weight:700;font-size:16px;text-decoration:none;width:180px}
.main-nav a.active{left:31px;top:12px;height:32px;width:106px;background:var(--red)}
.main-nav .sep{position:absolute;top:12px;width:1px;height:32px;background:#3a3a3a}

/* hero */
.hero{position:absolute;left:0;top:134px;width:1200px;height:474px;background:linear-gradient(180deg,#6e6656 0%,#8a7c62 45%,#5a5246 100%)}
.hero-caption{position:absolute;left:0;bottom:0;width:100%;height:92px;background:rgba(0,0,0,.45);text-align:center;color:var(--white)}
.hero-caption h1{font-family:"Open Sans",sans-serif;font-weight:700;font-size:25px;margin-top:12px;letter-spacing:.2px}
.hero-caption p{font-family:"Open Sans",sans-serif;font-weight:600;font-size:24px;margin-top:4px}
.slide-arrow{position:absolute;top:216px;width:42px;height:42px;background:rgba(0,0,0,.7);display:flex;align-items:center;justify-content:center}

/* welcome */
.welcome{position:absolute;left:0;top:608px;width:1200px;height:429px;background:var(--paper)}
.section-title{font-family:"Open Sans",sans-serif;font-weight:700;font-size:31px;line-height:40px}
.accent{color:var(--red)}
.rule{width:58px;height:3px;background:var(--red)}
.welcome .section-title{position:absolute;left:82px;top:40px;color:var(--ink)}
.welcome .rule{position:absolute;left:82px;top:139px}
.welcome-text{position:absolute;left:82px;top:169px;width:625px;font-size:14px;line-height:25.5px;color:#2a2a2a}
.btn-red{position:absolute;background:var(--red);color:var(--white);font-family:"Open Sans",sans-serif;font-weight:700;font-size:15px;display:flex;align-items:center;justify-content:center}
.welcome-photo{position:absolute;left:730px;top:65px;width:385px;height:364px;background:linear-gradient(160deg,#e2e8ee,#4a8fc4 60%,#2e6ea3)}

/* services */
.services{position:absolute;left:0;top:1037px;width:1200px;height:768px;background:linear-gradient(180deg,#1b1b1b,#2a2410 55%,#141414)}
.services .section-title{position:absolute;width:100%;top:48px;text-align:center;color:var(--white)}
.services .rule{position:absolute;left:571px;top:108px}
.service-grid{position:absolute;left:82px;top:162px;width:1038px;height:538px}
.grid-line{position:absolute;background:rgba(255,255,255,.14)}
.service{position:absolute;width:260px;text-align:center;color:var(--white);font-family:"Open Sans",sans-serif;font-size:20px;line-height:25px}
.service-icon{width:56px;height:56px;margin:0 auto 22px;background:var(--red);border-radius:6px}

/* testimonials */
.testimonials{position:absolute;left:0;top:1805px;width:1200px;height:436px;background:var(--white)}
.testimonials .section-title{position:absolute;width:100%;top:40px;text-align:center}
.quote-text{position:absolute;left:150px;top:130px;width:970px;text-align:center;font-style:italic;font-size:15px;line-height:30px;color:#333}
.quote-mark{position:absolute;font-family:"Open Sans",sans-serif;font-size:90px;line-height:90px;color:#bdbdbd}
.quote-line{position:absolute;left:234px;top:241px;width:739px;height:1px;background:#d5d5d5}
.quote-notch{position:absolute;left:593px;top:241px;width:12px;height:12px;border-right:1px solid #d5d5d5;border-bottom:1px solid #d5d5d5;background:var(--white);transform:translateY(-6px) rotate(45deg)}
.avatar{position:absolute;border-radius:50%;background:linear-gradient(160deg,#cfcfcf,#8c8c8c);border:3px solid #d8d8d8}
.avatar.current{border-color:var(--red)}
.client-name{position:absolute;width:100%;top:363px;text-align:center;color:var(--red);font-family:"Open Sans",sans-serif;font-size:18px}

/* footer */
.site-footer{position:absolute;left:0;top:2241px;width:1200px;height:312px;background:var(--night);color:var(--white)}
.footer-heading{position:absolute;top:33px;font-family:"Open Sans",sans-serif;font-weight:700;font-size:15px;letter-spacing:.5px}
.footer-heading::after{content:"";display:block;width:26px;height:2px;background:var(--red);margin-top:9px}
.quick-links{position:absolute;left:82px;top:86px;list-style:none;font-size:13px;line-height:33px}
.quick-links li::before{content:"› ";color:var(--red);font-weight:700}
.field{position:absolute;left:304px;width:247px;height:35px;border:1px solid #bfbfbf;font-size:12px;padding:8px 9px;color:var(--white)}
.submit{left:304px;top:239px;width:247px;height:35px}
.contact-item{position:absolute;left:669px;display:flex;gap:10px;font-size:13px;line-height:17px}
.contact-item svg{flex:none;margin-top:1px}
.footer-brand{position:absolute;left:1010px;top:82px;width:110px;display:flex;flex-direction:column;align-items:center;gap:8px;font-family:"Open Sans",sans-serif;font-weight:700;font-size:15px;color:#cfcfcf}
.footer-brand .sq{width:40px;height:40px;background:#cfcfcf}
.social{position:absolute;top:213px;width:32px;height:32px;border-radius:50%;background:var(--red)}
.copyright{position:absolute;left:0;top:2553px;width:1200px;height:52px;background:var(--red);color:var(--white);font-size:13px;display:flex;align-items:center;justify-content:center}
</style>
</head>
<body>

<header class="site-header">
  <div class="brand">
    <div class="brand-mark"></div>
    <div class="brand-name">Brightkeep<br>Cleaning Services</div>
  </div>
  <div class="top-contact" style="left:530px">
    <span class="ring"><svg width="14" height="14" viewBox="0 0 24 24"><path fill="#ec1f27" d="M6.6 10.8a15.1 15.1 0 0 0 6.6 6.6l2.2-2.2c.3-.3.7-.4 1-.2 1.1.4 2.3.6 3.6.6.6 0 1 .4 1 1V20c0 .6-.4 1-1 1A17 17 0 0 1 3 4c0-.6.4-1 1-1h3.5c.6 0 1 .4 1 1 0 1.3.2 2.5.6 3.6.1.3 0 .7-.2 1z"/></svg></span>
    <span>555-304-7162</span>
  </div>
  <div class="top-contact" style="left:680px;font-size:12px">
    <span class="ring"><svg width="14" height="12" viewBox="0 0 24 20"><rect x="1" y="2" width="22" height="16" rx="2" fill="none" stroke="#ec1f27" stroke-width="2.4"/><path d="M2 4l10 8 10-8" fill="none" stroke="#ec1f27" stroke-width="2.4"/></svg></span>
    <span>info@brightkeepcleaning.com</span>
  </div>
  <a class="quote-btn">Get A Free Quote</a>
  <nav class="main-nav">
    <a class="active">HOME</a>
    <a style="left:177px">ABOUT US</a>
    <span class="sep" style="left:364px"></span>
    <a style="left:374px">SERVICES</a>
    <span class="sep" style="left:564px"></span>
    <a style="left:582px">CONTACT US</a>
  </nav>
</header>

<section class="hero">
  <div class="abs" role="img" aria-label="Janitorial staff mopping the lobby floor of a commercial building beside wet floor signs" style="inset:0"></div>
  <div class="slide-arrow" style="left:17px"><svg width="12" height="18" viewBox="0 0 12 18"><path d="M10 2L3 9l7 7" fill="none" stroke="#fff" stroke-width="3"/></svg></div>
  <div class="slide-arrow" style="left:1139px"><svg width="12" height="18" viewBox="0 0 12 18"><path d="M2 2l7 7-7 7" fill="none" stroke="#fff" stroke-width="3"/></svg></div>
  <div class="hero-caption">
    <h1>WE OFFER JANITORIAL CLEANING PARTICULARLY FOR COMMERCIAL BUILDINGS</h1>
    <p>Serving All of Hudson, Valatie, Troy &amp; Albany</p>
  </div>
</section>

<section class="welcome">
  <h2 class="section-title">WELCOME TO<br><span class="accent">BRIGHTKEEP CLEANING SERVICES</span></h2>
  <div class="rule"></div>
  <p class="welcome-text">Lorem ipsum dolor sit amet, consectetuer adipiscing elit, sed diam nonummy nibh euismod tincidunt ut laoreet dolore magna aliquam erat volutpat. Ut wisi enim ad minim veniam, quis nostrud exerci tation ullamcorper suscipit lobortis nisl ut aliquip ex ea commodo consequat. Duis autem vel eum iriure dolor in hendrerit in vulputate velit esse molestie consequat, vel illum dolore eu feugiat nulla facilisis at vero eros et accumsan et iusto odio dignissim qui blandit praesent luptatum zzril delenit augue duis dolore te feugait nulla facilisi.</p>
  <a class="btn-red" style="left:82px;top:351px;width:120px;height:33px">Read More</a>
  <div class="welcome-photo" role="img" aria-label="Two smiling cleaners in blue aprons giving a thumbs up beside a vacuum"></div>
</section>

<section class="services">
  <div class="abs" role="img" aria-label="Dimmed background of a mop bucket and wet floor caution sign" style="inset:0;background:rgba(0,0,0,.35)"></div>
  <h2 class="section-title">OUR <span class="accent">SERVICES</span></h2>
  <div class="rule"></div>
  <div class="service-grid">
    <div class="grid-line" style="left:259px;top:0;width:1px;height:538px"></div>
    <div class="grid-line" style="left:519px;top:0;width:1px;height:538px"></div>
    <div class="grid-line" style="left:778px;top:0;width:1px;height:356px"></div>
    <div class="grid-line" style="left:0;top:156px;width:1038px;height:1px"></div>
    <div class="grid-line" style="left:0;top:352px;width:1038px;height:1px"></div>

    <div class="service" style="left:0;top:12px"><div class="service-icon" role="img" aria-label="Office cleaning pictogram"></div>General<br>Office Cleaning</div>
    <div class="service" style="left:260px;top:12px"><div class="service-icon" role="img" aria-label="Construction cleaning pictogram"></div>Construction<br>Cleaning</div>
    <div class="service" style="left:519px;top:12px"><div class="service-icon" role="img" aria-label="Carpet extraction pictogram"></div>Carpet<br>Extraction</div>
    <div class="service" style="left:778px;top:12px"><div class="service-icon" role="img" aria-label="Business consultation pictogram"></div>Consultation<br>/Business</div>

    <div class="service" style="left:0;top:206px"><div class="service-icon" role="img" aria-label="Lighting maintenance pictogram"></div>Lighting<br>Maintenance</div>
    <div class="service" style="left:260px;top:206px"><div class="service-icon" role="img" aria-label="Floor waxing pictogram"></div>Floor Striping<br>and Waxing</div>
    <div class="service" style="left:519px;top:206px"><div class="service-icon" role="img" aria-label="Window cleaning pictogram"></div>Window<br>Cleaning</div>
    <div class="service" style="left:778px;top:206px"><div class="service-icon" role="img" aria-label="Event cleaning pictogram"></div>Event<br>Cleaning</div>

    <div class="service" style="left:260px;top:404px"><div class="service-icon" role="img" aria-label="Floor and carpet cleaning pictogram"></div>Floor and Carpet<br>Cleaning</div>
    <div class="service" style="left:519px;top:404px"><div class="service-icon" role="img" aria-label="Seasonal deep cleaning pictogram"></div>Seasonal<br>Deep Cleaning</div>
  </div>
</section>

<section class="testimonials">
  <h2 class="section-title">CLIENT <span class="accent">TESTIMONIALS</span></h2>
  <span class="quote-mark" style="left:90px;top:110px">&ldquo;</span>
  <p class="quote-text">Lorem ipsum dolor sit amet, consectetuer adipiscing elit, sed diam nonummy nibh the is euismod tincidunt ut laoreet dolore magna aliquam erat volutpat. Ut wisi enim ad minim veniam, quis nostrud exerci tation ullamcorper suscipit lobortis nisl ut aliquip ex ea the commodo consequat. Duis autem vel eum iriure dolor in hendrerit in vulputate velit esse molestie consequat, vel illum dolore eu feugiat nulla</p>
  <span class="quote-mark" style="left:1030px;top:168px">&rdquo;</span>
  <div class="quote-line"></div>
  <div class="quote-notch"></div>
  <div class="avatar" role="img" aria-label="Client portrait" style="left:475px;top:271px;width:74px;height:74px"></div>
  <div class="avatar current" role="img" aria-label="Client portrait" style="left:560px;top:267px;width:78px;height:78px"></div>
  <div class="avatar" role="img" aria-label="Client portrait" style="left:649px;top:271px;width:74px;height:74px"></div>
  <p class="client-name">Lorem Ispum</p>
</section>

<footer class="site-footer">
  <h3 class="footer-heading" style="left:82px">QUICK LINKS</h3>
  <ul class="quick-links">
    <li>Home</li><li>About us</li><li>services</li><li>Contact us</li>
  </ul>

  <h3 class="footer-heading" style="left:304px">QUICK INQUIRY</h3>
  <div class="field" style="top:87px">Email</div>
  <div class="field" style="top:137px">Phone</div>
  <div class="field" style="top:187px">Message</div>
  <a class="btn-red submit">Submit</a>

  <h3 class="footer-heading" style="left:669px">CONTACT DETAILS</h3>
  <div class="contact-item" style="top:95px">
    <svg width="12" height="16" viewBox="0 0 12 16"><path fill="#ec1f27" d="M6 0a6 6 0 0 0-6 6c0 4.5 6 10 6 10s6-5.5 6-10a6 6 0 0 0-6-6zm0 8.5A2.5 2.5 0 1 1 6 3.5a2.5 2.5 0 0 1 0 5z"/></svg>
    <div><strong>Brightkeep Cleaning Services</strong><br>Lorem Ipsum Helps You Lismarter,<br>Giving You Time To Focus-123</div>
  </div>
  <div class="contact-item" style="top:166px">
    <svg width="14" height="14" viewBox="0 0 24 24"><path fill="#ec1f27" d="M6.6 10.8a15.1 15.1 0 0 0 6.6 6.6l2.2-2.2c.3-.3.7-.4 1-.2 1.1.4 2.3.6 3.6.6.6 0 1 .4 1 1V20c0 .6-.4 1-1 1A17 17 0 0 1 3 4c0-.6.4-1 1-1h3.5c.6 0 1 .4 1 1 0 1.3.2 2.5.6 3.6.1.3 0 .7-.2 1z"/></svg>
    <span>555-304-7162</span>
  </div>
  <div class="contact-item" style="top:203px">
    <svg width="14" height="14" viewBox="0 0 24 24"><rect x="2" y="6" width="20" height="14" rx="2" fill="#ec1f27"/><rect x="6" y="2" width="12" height="5" fill="#ec1f27"/></svg>
    <span>555-304-7162</span>
  </div>
  <div class="contact-item" style="top:241px">
    <svg width="14" height="12" viewBox="0 0 24 20"><rect x="1" y="2" width="22" height="16" rx="2" fill="#ec1f27"/><path d="M2 4l10 8 10-8" fill="none" stroke="#0b0b0b" stroke-width="2"/></svg>
    <span>info@brightkeepcleaning.com</span>
  </div>

  <div class="footer-brand"><div class="sq"></div>Brightkeep</div>
  <span class="social" style="left:1012px"></span>
  <span class="social" style="left:1051px"></span>
  <span class="social" style="left:1089px"></span>
</footer>

<div class="copyright">Copyright © 2017 Brightkeep Cleaning Services. All Rights Reserved.</div>

</body>
</html>
```